BrightLoop (1 page) homepage re-design

Our homepage needs a face-lift! We need our homepage on our website re-designed with a fresh and current look and feel. We have all the details, colour codes and a rough wireframe ready, but need a talented designer to put some personality into our ideas.

What we do: BrightLoop is a digital marketing agency with offices in Australia (Sydney) and South Africa (Cape Town). We specialise in SEO, PPC (otherwise known as Zentro PayLine or SEM), content marketing and Zentro Tallyboard. We use these tools to help our clients realise their business dreams.

VISUAL

Style / theme of the design:
Clean, simplistic, fun, flow.

Websites we draw inspiration from:
This is the theme we want to use to build the website
http://demo.vormalayouts.example/vl/?theme=Pebbled
Inspiration:
https://www.ondrapromo.example/
https://www.nelvagrowth.example.au/
https://quimbel.example.au/
https://torvin.layout-works.example/forum/

What we like about the site:
Clean, simple design, good use of white space. The subtle changing background colours, strong contrast with text. Not too busy or distracting.

What we don’t want: Too many different colours.

Target Market(s)

Our target audience: Marketing Managers of small to medium size businesses in Australia.

Industry/Entity Type

Marketing

Number of Pages Required

1 page

Font styles to use
Sans Serif

Requirements
Must have
• Elements to be added on homepage in order and as seen in attachments:
• - Section 1: Video with team as image and a play button add the heading: We help smart marketing managers achieve their KPIs [line break] and reduce their digital marketing overwhelm.
• - Section 2: Solutions section with the 6 solutions displayed in a row.
• - Section 3: Register Free Webinar with video
• - Section 4: Please add 3 case studies (as seen in attached docs there is only 1 but please add 3 below each other)
• - Section 5: Clients. Please add all client logo’s (black and white)
• - Section 6: Our Blog (as seen attached)
• - Section 7: Conferences Attended (please add the title and a paragraph of lorem Ipsom below) and then please add all conference logo’s attached below.
• - Section 8: In The Media (please add all logo’s titled media) white background
• - Section 9: Footer (dark grey footer) add our Zentro honoured affiliate logo here please
• - Section10: Footer - include:
• - Social logos (WorkMesh, Blipster, Pallwall, ReelDrop, Zentro Hub)
• - Navigation
• - Contact details (name, address, phone number, email)
• Colour codes:
• We want to use light greys, white and charcoal grey for the backgrounds with a pop of our green colour to bring out our branding and all CTA’s to be orange, colour codes below:
• Light grey: #F2F2F2
• Charcoal grey: #161616
• Green: #428E29
• CTA’s: #de7532
• PLEASE NOTE: Please see attached pdf titled: homepagecopybrief.pdf for all the titles and statistics that need to go on the homepage
Should not have
• Too much colour, icons should not be different colours

```html
<!DOCTYPE html>
<html lang="en">
<head>
<meta charset="utf-8">
<title>BrightLoop — Homepage</title>
<link rel="stylesheet" href="https://fonts.googleapis.com/css2?family=Lato:wght@300;400&family=Montserrat:wght@400;600&display=swap">
<style>
  :root {
    --green: #1a9a1a;
    --green-deep: #2f6e2a;
    --green-soft: #c9f2c9;
    --light-grey: #f2f2f2;
    --charcoal: #161616;
    --nav-text: #262626;
    --white: #ffffff;
  }
  * { margin: 0; padding: 0; box-sizing: border-box; }
  html, body { width: 1200px; height: 750px; overflow: hidden; background: var(--white); }
  .page { position: relative; width: 1200px; height: 750px; overflow: hidden; font-family: "Montserrat", sans-serif; }

  .topbar {
    position: absolute; top: 0; left: 0; width: 100%; height: 38px;
    background: var(--light-grey); border-bottom: 1px solid #d6d6d6;
    font-size: 13px; color: var(--charcoal); z-index: 3;
  }
  .topbar-item { position: absolute; top: 0; height: 38px; display: flex; align-items: center; gap: 8px; }
  .topbar-phone { left: 512px; }
  .topbar-address { left: 746px; font-size: 12.5px; }
  .topbar-item svg { width: 20px; height: 20px; }

  .hero-photo {
    position: absolute; top: 38px; left: 0; width: 100%; height: 640px;
    background:
      radial-gradient(ellipse at 55% 40%, rgba(170,220,170,0.55), transparent 45%),
      radial-gradient(ellipse at 15% 30%, rgba(120,190,120,0.5), transparent 40%),
      radial-gradient(ellipse at 90% 55%, rgba(150,200,170,0.45), transparent 40%),
      linear-gradient(160deg, #5b8f58 0%, #3f6e3d 45%, #466f48 70%, #557d55 100%);
  }

  .header {
    position: absolute; top: 38px; left: 0; width: 100%; height: 81px;
    background: rgba(242,242,242,0.82); z-index: 2;
  }
  .brand { position: absolute; left: 171px; top: 26px; display: flex; align-items: center; gap: 8px; }
  .brand-mark { width: 26px; height: 26px; background: var(--green); }
  .brand-name { font-family: "Lato", sans-serif; font-weight: 400; font-size: 27px; letter-spacing: 2px; color: var(--green); }
  .nav { position: absolute; left: 500px; top: 32px; display: flex; gap: 14.5px; list-style: none; }
  .nav li { font-size: 11px; font-weight: 600; color: var(--nav-text); letter-spacing: 0.2px; }

  .hero-heading {
    position: absolute; top: 268px; left: 0; width: 1200px; text-align: center;
    font-family: "Lato", sans-serif; font-weight: 300; font-size: 37px; line-height: 51px;
    color: var(--white); letter-spacing: -0.5px; text-transform: uppercase;
    text-shadow: 0 1px 3px rgba(0,0,0,0.25); z-index: 2;
  }

  .hero-wave { position: absolute; left: 0; top: 560px; width: 1200px; height: 190px; z-index: 1; }
  .play-button { position: absolute; left: 559px; top: 567px; width: 78px; height: 78px; z-index: 2; }

  .solutions-title {
    position: absolute; top: 700px; left: 0; width: 1200px; text-align: center;
    font-family: "Lato", sans-serif; font-weight: 400; font-size: 29px; color: var(--green);
    text-transform: uppercase; letter-spacing: -0.3px; z-index: 2;
  }
</style>
</head>
<body>
<div class="page">
  <div class="topbar">
    <div class="topbar-item topbar-phone">
      <svg viewBox="0 0 24 24" fill="none" stroke="#1a9a1a" stroke-width="1.8" stroke-linecap="round" stroke-linejoin="round">
        <path d="M5 3h3l2 5-2 1.5a11 11 0 0 0 6.5 6.5L16 14l5 2v3a2 2 0 0 1-2 2A17 17 0 0 1 3 5a2 2 0 0 1 2-2z"/>
        <path d="M14 3a7 7 0 0 1 7 7M14 7a3 3 0 0 1 3 3"/>
      </svg>
      <span>1300 555 014</span>
    </div>
    <div class="topbar-item topbar-address">
      <svg viewBox="0 0 24 24" fill="none" stroke="#1a9a1a" stroke-width="1.8">
        <path d="M12 22s7-7.5 7-13a7 7 0 0 0-14 0c0 5.5 7 13 7 13z"/>
        <circle cx="12" cy="9" r="2.6"/>
      </svg>
      <span>24-26 Harbourline St, Millers Point, Sydney</span>
    </div>
  </div>

  <div class="hero-photo" role="img" aria-label="Overhead photo of a team working around a desk with laptops, papers and charts, tinted green"></div>

  <header class="header">
    <div class="brand">
      <span class="brand-mark"></span>
      <span class="brand-name">BRIGHTLOOP</span>
    </div>
    <ul class="nav">
      <li>HOME</li><li>ABOUT</li><li>PPC</li><li>SEO</li><li>TRAINING</li>
      <li>CLIENT SUCCESS</li><li>BLOG</li><li>RESOURCES</li><li>CONTACT</li>
    </ul>
  </header>

  <h1 class="hero-heading">How confident are you in<br>achieving your revenue target</h1>

  <svg class="hero-wave" viewBox="0 0 1200 190" preserveAspectRatio="none">
    <path d="M0 120 C 120 170, 260 150, 380 110 C 500 70, 560 30, 640 45 C 720 60, 760 110, 880 100 C 1000 90, 1080 20, 1200 40 L1200 190 L0 190 Z" fill="#c9f2c9"/>
    <path d="M0 140 C 120 185, 260 165, 380 125 C 500 85, 560 50, 640 62 C 720 75, 760 125, 880 115 C 1000 105, 1080 40, 1200 62 L1200 190 L0 190 Z" fill="#ffffff"/>
  </svg>

  <svg class="play-button" viewBox="0 0 78 78" role="button" aria-label="Play video">
    <circle cx="39" cy="39" r="38" fill="#ffffff"/>
    <circle cx="39" cy="39" r="33" fill="#1a9a1a"/>
    <circle cx="39" cy="39" r="26" fill="none" stroke="#ffffff" stroke-width="2.5"/>
    <path d="M32 27 L53 39 L32 51 Z" fill="#ffffff"/>
  </svg>

  <h2 class="solutions-title">Our Solutions</h2>
</div>
</body>
</html>
```